New Zealand Export company needs business cards

We need new business cards to match our new logo for a company based in New Zealand who deal specifically with the Pacific Islands. We source, consolidate and ship products out of New Zealand to the Pacific Islands. Will attach our old ones and also new logo.
Would like the Islands we deal with and the areas of work we have access to, to be included on the business cards.

Contact Information for Business Card

T +64 9 571 3048
F +64 9 571 6285
12-18 Kowhai Lane, Drury, 2113
PO Box 814, Drury, Auckland 2247, New Zealand
www.falconfreight.example.nz
E sales@falconfreight.example.nz

Font styles to use
Sans Serif

Colors
85abd2
33a6d7
ffffff

Requirements
Must have
• A company of PWM

```html
<!DOCTYPE html>
<html lang="en">
<head>
<meta charset="utf-8">
<title>Falcon Freight – Business Card</title>
<link rel="stylesheet" href="https://fonts.googleapis.com/css2?family=Montserrat:wght@500;600;700&display=swap">
<style>
  :root {
    --sky-blue: #85abd2;
    --ocean-blue: #33a6d7;
    --white: #ffffff;
    --stage: #e8edf1;
    --photo-top: #8fb6c8;
    --photo-mid: #4f8fa8;
    --photo-island: #4f7a3e;
    --photo-sea: #2f7f99;
  }
  * { box-sizing: border-box; margin: 0; padding: 0; }
  html, body { width: 711px; height: 1200px; overflow: hidden; }
  body {
    background: var(--stage);
    font-family: "Montserrat", Arial, sans-serif;
    position: relative;
  }
  .card {
    position: absolute;
    width: 472px;
    height: 270px;
    overflow: hidden;
    box-shadow: 0 6px 14px rgba(0, 0, 0, 0.25);
  }

  /* Front */
  .card-front { left: 129px; top: 61px; }
  .front-photo {
    position: absolute; inset: 0;
    background:
      radial-gradient(ellipse 45% 40% at 52% 55%, var(--photo-island) 0%, rgba(79,122,62,0.6) 55%, rgba(79,122,62,0) 100%),
      linear-gradient(180deg, var(--photo-top) 0%, var(--photo-mid) 60%, var(--photo-sea) 100%);
  }
  .front-stripes { position: absolute; inset: 0; }
  .front-brand {
    position: absolute; left: 0; right: 0; top: 96px;
    display: flex; align-items: center; justify-content: center; gap: 12px;
    color: var(--white);
  }
  .brand-square { width: 26px; height: 26px; background: var(--white); }
  .front-brand .brand-name {
    font-weight: 700; font-size: 40px; letter-spacing: 1px; line-height: 1;
  }
  .tagline {
    position: absolute; left: 0; right: 0; top: 163px;
    text-align: center; color: var(--white);
    font-weight: 500; font-size: 23px;
  }

  /* Back */
  .card-back { left: 128px; top: 380px; background: var(--white); }
  .back-stripes { position: absolute; inset: 0; }
  .back-brand {
    position: absolute; left: 27px; top: 33px;
    display: flex; align-items: center; gap: 10px;
    color: var(--sky-blue);
  }
  .back-brand .brand-square { width: 22px; height: 22px; background: var(--sky-blue); }
  .back-brand .brand-name { font-weight: 700; font-size: 27px; letter-spacing: 1px; line-height: 1; }
  .person { position: absolute; left: 133px; top: 112px; }
  .person-name {
    display: inline-block;
    font-weight: 600; font-size: 34px; line-height: 1.05;
    color: var(--ocean-blue);
    border-bottom: 1.5px solid var(--sky-blue);
  }
  .person-role { font-weight: 500; font-size: 9.5px; color: var(--ocean-blue); margin-top: 4px; }
  .contact { position: absolute; font-weight: 500; font-size: 9.2px; color: var(--ocean-blue); line-height: 1.3; }
  .contact-row { display: flex; align-items: center; gap: 8px; position: absolute; white-space: nowrap; }
  .contact-row svg { flex: none; }
</style>
</head>
<body>

<section class="card card-front" aria-label="Card front">
  <div class="front-photo" role="img" aria-label="Photograph of a green rocky island in a blue sea under a cloudy sky"></div>
  <svg class="front-stripes" width="472" height="270" viewBox="0 0 472 270" aria-hidden="true">
    <g fill="#ffffff">
      <rect x="11" y="175" width="12" height="95"/>
      <rect x="34" y="185" width="12" height="85"/>
      <rect x="57" y="195" width="12" height="75"/>
      <rect x="80" y="205" width="12" height="65"/>
      <rect x="103" y="215" width="12" height="55"/>
      <rect x="126" y="225" width="12" height="45"/>
      <rect x="149" y="235" width="12" height="35"/>
      <rect x="172" y="245" width="12" height="25"/>
      <rect x="195" y="254" width="12" height="16"/>
      <rect x="218" y="262" width="12" height="8"/>
    </g>
  </svg>
  <div class="front-brand">
    <span class="brand-square"></span>
    <span class="brand-name">FALCON FREIGHT</span>
  </div>
  <p class="tagline">A company of PWM</p>
</section>

<section class="card card-back" aria-label="Card back">
  <svg class="back-stripes" width="472" height="270" viewBox="0 0 472 270" aria-hidden="true">
    <g fill="#33a6d7">
      <rect x="451" y="0" width="11" height="92"/>
      <rect x="428" y="0" width="11" height="84"/>
      <rect x="405" y="0" width="11" height="75"/>
      <rect x="382" y="0" width="11" height="66"/>
      <rect x="359" y="0" width="11" height="57"/>
      <rect x="336" y="0" width="11" height="47"/>
      <rect x="313" y="0" width="11" height="37"/>
      <rect x="290" y="0" width="11" height="27"/>
      <rect x="267" y="0" width="11" height="16"/>
      <rect x="244" y="0" width="11" height="6"/>
    </g>
  </svg>

  <div class="back-brand">
    <span class="brand-square"></span>
    <span class="brand-name">FALCON FREIGHT</span>
  </div>

  <div class="person">
    <h1 class="person-name">Tessa Hale</h1>
    <p class="person-role">Sales Manager</p>
  </div>

  <div class="contact">
    <div class="contact-row" style="left:21px; top:202px;">
      <svg width="12" height="14" viewBox="0 0 12 14"><path d="M6 0a5 5 0 0 0-5 5c0 3.6 5 9 5 9s5-5.4 5-9a5 5 0 0 0-5-5zm0 7a2 2 0 1 1 0-4 2 2 0 0 1 0 4z" fill="#85abd2"/></svg>
      <span>12-18 Kowhai Lane, Drury, 2113<br>PO Box 814, Drury, Auckland 2247, New Zealand</span>
    </div>
    <div class="contact-row" style="left:21px; top:230px;">
      <svg width="12" height="13" viewBox="0 0 24 24"><path d="M6.6 10.8a15.1 15.1 0 0 0 6.6 6.6l2.2-2.2a1 1 0 0 1 1-.25 11.4 11.4 0 0 0 3.6.6 1 1 0 0 1 1 1V20a1 1 0 0 1-1 1A17 17 0 0 1 3 4a1 1 0 0 1 1-1h3.5a1 1 0 0 1 1 1c0 1.25.2 2.45.6 3.6a1 1 0 0 1-.25 1z" fill="#85abd2"/></svg>
      <span>+64 9 571 3048</span>
    </div>
    <div class="contact-row" style="left:293px; top:205px;">
      <svg width="16" height="16" viewBox="0 0 16 16" fill="none" stroke="#85abd2" stroke-width="1"><circle cx="8" cy="8" r="7"/><ellipse cx="8" cy="8" rx="3" ry="7"/><path d="M1 8h14M2.5 4.5h11M2.5 11.5h11"/></svg>
      <span>www.falconfreight.example.nz</span>
    </div>
    <div class="contact-row" style="left:293px; top:230px;">
      <svg width="16" height="14" viewBox="0 0 16 14"><rect width="16" height="14" rx="1.5" fill="#85abd2"/><path d="M2 3l6 5 6-5" fill="none" stroke="#ffffff" stroke-width="1.4"/></svg>
      <span>Esales@falconfreight.example.nz</span>
    </div>
  </div>
</section>

</body>
</html>
```